Marcelo Quintana Postcard/Rack Card

Marcelo Quintana
Tenor & Vocal Coach
mqvoice@brivamail.com
(713) 582-6031
www.voicefromthecore.com
Want two sided postcard / rack card.4" x 9"
Front - vertical - picture in t-shirt, name, title (Tenor & Vocal Coach), contact information
Back - horizontal - picture in jacket, name, title (Tenor & Vocal Coach), contact information, bio (see attachment for words)
Do not leave space for an address.
Looking for an edgy modern design!

Target Market(s)

Young adults

Requirements
Nice to have
• Will pay extra to get a complimentary business card design, two sided

```html
<!DOCTYPE html>
<html lang="en">
<head>
<meta charset="utf-8">
<title>Marcelo Quintana – Tenor &amp; Vocal Coach</title>
<link rel="stylesheet" href="https://fonts.googleapis.com/css2?family=Audiowide&family=Bebas+Neue&family=Arimo:wght@400;700&family=Roboto+Condensed:wght@700&display=swap">
<style>
  :root {
    --pink-hot: #f43fa6;
    --pink-mid: #e0248f;
    --magenta-deep: #b3127f;
    --purple-deep: #8e1579;
    --navy: #1c2170;
    --white: #ffffff;
    --yellow: #fff200;
    --frame: #ffffff;
  }
  * { margin: 0; padding: 0; box-sizing: border-box; }
  html, body {
    width: 1200px; height: 551px; overflow: hidden;
    background: var(--purple-deep);
  }
  .card {
    position: relative; width: 1200px; height: 551px; overflow: hidden;
    background:
      radial-gradient(ellipse 600px 260px at 820px 90px, rgba(255,120,200,0.55), transparent 70%),
      linear-gradient(90deg, rgba(120,10,100,0.45) 0%, transparent 40%),
      linear-gradient(180deg, var(--pink-hot) 0%, var(--pink-mid) 35%, var(--magenta-deep) 75%, var(--purple-deep) 100%);
  }
  .portrait-frame {
    position: absolute; left: 67px; top: 67px; width: 389px; height: 418px;
    background: var(--frame); padding: 11px;
    box-shadow: 0 6px 18px rgba(60,0,50,0.45);
  }
  .portrait {
    width: 100%; height: 100%;
    background:
      linear-gradient(180deg, #c9c6a4 0%, #b6b38c 45%, #3c4a6e 70%, #1f2a4e 100%);
  }
  .name {
    position: absolute; left: 456px; width: 744px; top: 84px;
    text-align: center;
    font-family: "Audiowide", sans-serif;
    font-size: 44px; line-height: 1; letter-spacing: 1px;
    color: var(--white); text-transform: uppercase;
  }
  .title {
    position: absolute; left: 456px; width: 744px; top: 138px;
    text-align: center;
    font-family: "Bebas Neue", sans-serif;
    font-size: 41px; line-height: 1; letter-spacing: 0.5px;
    color: var(--yellow);
  }
  .bio {
    position: absolute; left: 456px; top: 198px; width: 744px; height: 212px;
    background: var(--navy);
    padding: 17px 40px 0;
    text-align: center;
    font-family: "Arimo", sans-serif;
    font-size: 19px; line-height: 28px; color: var(--white);
  }
  .bio p + p { margin-top: 8px; }
  .contact {
    position: absolute; left: 456px; width: 744px; top: 428px;
    text-align: center;
  }
  .contact-lead {
    font-family: "Arimo", sans-serif; font-weight: 700;
    font-size: 17.5px; line-height: 1.2; color: var(--yellow);
  }
  .contact-lead .contact-name { color: var(--white); }
  .contact-details {
    margin-top: 3px;
    font-family: "Roboto Condensed", sans-serif; font-weight: 700;
    font-size: 37px; line-height: 1.15; color: var(--white);
  }
</style>
</head>
<body>
  <main class="card">
    <div class="portrait-frame">
      <div class="portrait" role="img" aria-label="Portrait photo of Marcelo Quintana in a navy jacket and white shirt"></div>
    </div>

    <h1 class="name">Marcelo Quintana</h1>
    <h2 class="title">Tenor &amp; Vocal Coach</h2>

    <section class="bio">
      <p>Marcelo is a local singer and actor who has been working professionally around the country as a concert artist and musical theater performer.</p>
      <p>He studied at the Delmont School of Music, Bayfield University and works as a vocal coach with local youths and adults in Houston area.</p>
      <p>Marcelo’s goal is to help his students master their individual instrument so that they can achieve a natural and effortless vocal production.</p>
    </section>

    <section class="contact">
      <p class="contact-lead">For more information please contact <span class="contact-name">Marcelo today!</span></p>
      <p class="contact-details">mqvoice@brivamail.com • (713) 582-6031</p>
    </section>
  </main>
</body>
</html>
```